Private Optometric Practice Needs new Presentation Folders/Stationary

We recently moved our office and are looking to refresh our presentation folders and stationary. I tend to prefer simple, clean designs. We are a full scope optometric practice provide high quality eyewear, custom contact lenses, along with emergency care and treatment for dry eyes. We communicate with a lot of other doctors and want to exude professionalism. I have attached 2 versions of our logo.

Target Market(s)

Familys

Industry/Entity Type

Eyecare

Font styles to use
Sans Serif

Colors
0054AA
0677BA
7BADD7
CADEEF
E8F1F8

Requirements
Nice to have
• Bifold, areas to put information about practice, welcome letter

```html
<!DOCTYPE html>
<html lang="en">
<head>
<meta charset="utf-8">
<title>Clearview Optics – Stationery</title>
<link href="https://fonts.googleapis.com/css2?family=Montserrat:wght@400&family=Open+Sans:wght@400;600&display=swap" rel="stylesheet">
<style>
:root{
  --bg:#b8b8b8;
  --navy:#0c1a28;
  --blue:#3aa8df;
  --white:#ffffff;
  --ink:#1c1c1c;
  --muted:#555;
  --line:#2a2a2a;
  --field:#dcdcdc;
}
*{margin:0;padding:0;box-sizing:border-box}
html,body{width:1200px;height:627px;overflow:hidden}
body{background:var(--bg);position:relative;font-family:'Open Sans',sans-serif;color:var(--ink)}
.sheet{position:absolute;background:var(--white);overflow:hidden;box-shadow:0 1px 3px rgba(0,0,0,.25)}
.wave{position:absolute;left:0;bottom:0;width:100%;display:block}
.brand{font-family:'Montserrat',sans-serif;font-weight:400;text-transform:uppercase;text-align:center;line-height:1.15;display:flex;flex-direction:column;align-items:center}
.brand .dot{border-radius:50%;background:var(--blue);margin-bottom:3px}
.brand-light{color:var(--white)}
.brand-dark{color:var(--navy)}

/* letterhead */
.letterhead{left:63px;top:103px;width:190px;height:269px}
.letterhead .head{height:43px;background:var(--navy);position:relative}
.letterhead .brand{position:absolute;left:8px;top:6px;width:55px;font-size:5.6px;letter-spacing:1.6px}
.letterhead .brand .dot{width:10px;height:10px}
.head-contact{position:absolute;left:135px;top:10px;border-left:1px solid var(--blue);padding-left:4px;color:var(--white);font-size:3.3px;line-height:1.35}
.letter{padding:18px 9px 0;font-size:3.4px;line-height:1.35}
.letter p{margin-bottom:4px}
.letter .salute{font-size:4.4px;font-weight:600;margin:5px 0 4px}
.signature{width:42px;height:9px;background:linear-gradient(90deg,#cfcfcf,#e6e6e6);margin-top:14px}

/* folder */
.folder{left:318px;top:103px;width:240px;height:130px;display:flex}
.folder .panel{width:50%;height:100%;position:relative;overflow:hidden}
.folder .back{background:var(--navy)}
.folder .front{background:var(--white)}
.folder .back .brand{position:absolute;left:0;right:0;top:28px;font-size:10px;letter-spacing:3px}
.folder .back .brand .dot{width:20px;height:20px}
.folder .back .foot{position:absolute;left:0;right:0;bottom:10px;color:var(--white);font-size:3.6px;text-align:center;line-height:1.5}
.folder .front .mark{position:absolute;left:50%;top:32px;transform:translateX(-50%);width:46px;height:46px;border-radius:50%;background:var(--blue)}
.folder-inside{left:318px;top:245px;width:240px;height:127px;display:flex}
.folder-inside .panel{width:50%;height:100%;position:relative;background:#e9e9e9}
.folder-inside .pocket-l{position:absolute;left:0;right:0;bottom:0;height:42px;background:var(--navy)}
.folder-inside .pocket-r{position:absolute;left:0;right:0;bottom:0;height:42px;background:var(--blue)}
.folder-inside .insert{position:absolute;left:12px;top:8px;width:90px;height:110px;background:var(--white)}
.folder-inside .insert .bar{height:15px;background:var(--navy)}

/* envelope */
.envelope{left:595px;top:103px;width:195px;height:85px}
.envelope .flap{height:25px;background:var(--navy);border-radius:0 0 12px 12px;display:flex;align-items:center;justify-content:center}
.envelope .flap .dot{width:13px;height:13px;border-radius:50%;background:var(--blue)}

/* compliment slip */
.slip{left:595px;top:228px;width:195px;height:85px}
.slip .brand{position:absolute;left:6px;top:7px;width:30px;font-size:3.6px;letter-spacing:1px}
.slip .brand .dot{width:8px;height:8px;margin-bottom:2px}
.slip .addr{position:absolute;left:42px;top:9px;border-left:1px solid var(--blue);padding-left:4px;font-size:3px;line-height:1.35;height:16px}

/* business cards */
.card{top:423px;height:100px}
.card-front{left:63px;width:175px}
.card-front .brand{position:absolute;left:16px;top:28px;width:80px;font-size:10px;letter-spacing:2.5px}
.card-front .brand .dot{width:20px;height:20px}
.person{position:absolute;border-left:1px solid var(--blue);font-size:4.6px;line-height:1.45;color:var(--muted)}
.person .name{font-family:'Open Sans',sans-serif;font-weight:600;color:var(--blue);font-size:7.4px;line-height:1.2}
.person .role{margin-bottom:4px}
.person .gap{margin-top:4px}
.ico{display:inline-block;width:3.6px;height:3.6px;border-radius:50%;background:var(--blue);margin-right:2px;vertical-align:middle}
.card-front .person{left:95px;top:24px;padding-left:6px;height:56px}
.card-front .stripe{position:absolute;left:0;bottom:0;width:100%;height:8px;background:var(--blue)}
.card-front .stripe::before{content:"";position:absolute;left:0;top:0;width:55%;height:3px;background:var(--navy)}
.card-back{left:298px;width:175px;background:var(--navy);border-radius:8px}
.card-back .brand{position:absolute;left:0;right:0;top:14px;font-size:18px;letter-spacing:5px}
.card-back .brand .dot{width:34px;height:34px;margin-bottom:6px}
.card-wide{left:540px;width:239px;top:430px;height:93px}
.card-wide .brand{position:absolute;left:40px;top:16px;width:70px;font-size:8.8px;letter-spacing:2.3px}
.card-wide .brand .dot{width:19px;height:19px}
.card-wide .socials{position:absolute;left:61px;top:72px;display:flex;gap:1.5px}
.card-wide .socials span{width:5px;height:5px;border-radius:50%;background:var(--blue)}
.card-wide .person{left:115px;top:15px;padding-left:8px;height:68px;font-size:6px}
.card-wide .person .name{font-size:8.8px}

/* invoice */
.invoice{left:841px;top:103px;width:297px;height:420px}
.invoice .head{height:78px;background:var(--navy);position:relative}
.invoice .brand{position:absolute;left:28px;top:16px;width:80px;font-size:11px;letter-spacing:3px}
.invoice .brand .dot{width:22px;height:22px}
.invoice .title{position:absolute;right:27px;top:33px;color:var(--white);font-weight:600;font-size:13px}
.inv-info{position:absolute;top:107px;font-size:5px;line-height:1.45}
.inv-office{left:28px}
.inv-contact{left:94px}
.inv-order{position:absolute;left:198px;top:97px;width:71px;height:30px;background:var(--navy);border-radius:2px;color:var(--white);font-size:4.6px;line-height:1.55;padding:4px 5px}
.inv-table{position:absolute;left:28px;top:160px;width:241px;border-collapse:collapse;font-size:5px}
.inv-table th{background:var(--blue);color:var(--white);font-weight:400;height:12px;border:1px solid var(--white)}
.inv-table td{height:12px;border:.8px solid var(--line)}
.totals{position:absolute;right:27px;top:308px;font-size:7px;text-align:right}
.totals .row{display:flex;align-items:center;justify-content:flex-end;gap:6px;height:13px;margin-bottom:0}
.totals .box{width:45px;height:10px;background:var(--field)}
.totals .row.total{margin-top:5px}
.totals .row.total .box{background:var(--white);border:1px solid var(--line);height:15px}
.terms{position:absolute;left:28px;top:320px;border-left:3px solid var(--blue);padding-left:5px;font-size:3.6px;line-height:1.35;width:120px}
.sign{position:absolute;top:370px;width:70px;border-top:.8px solid var(--line);font-size:3.8px;text-align:center;padding-top:2px}
.sign-recv{left:28px}
.sign-auth{left:122px}
</style>
</head>
<body>

<!-- letterhead -->
<section class="sheet letterhead">
  <header class="head">
    <div class="brand brand-light"><span class="dot"></span>Clearview<br>Optics</div>
    <div class="head-contact">Your address, City<br>State, Zip 1234<br>123 456 789<br>info@yourgmail.com<br>www.yourwebsite.com</div>
  </header>
  <div class="letter">
    <p>January-03-2020</p>
    <p>Mr, Mark Ellis<br>President</p>
    <p>Harbor Group<br>123 Street Name, Suite# 10<br>City, State, 120023</p>
    <p class="salute">Dear Mr, Ellis</p>
    <p>Thank you for choosing our practice for your family's eye care. We look forward to seeing you soon.</p>
    <p>Our team offers full eye exams, custom contact lenses, quality eyewear and dry eye treatment.</p>
    <p>Please call us with any questions before your visit.</p>
    <p>Regards</p>
    <div class="signature" role="img" aria-label="Handwritten signature of Laura Bennett"></div>
  </div>
  <svg class="wave" viewBox="0 0 190 22" preserveAspectRatio="none" height="22"><path d="M0 14 C40 0 80 4 120 12 S170 18 190 4 L190 22 L0 22Z" fill="#0c1a28"/><path d="M0 16 C40 4 80 8 120 16 S170 20 190 10 L190 22 L0 22Z" fill="#3aa8df"/></svg>
</section>

<!-- folder cover spread -->
<section class="sheet folder">
  <div class="panel back">
    <div class="brand brand-light"><span class="dot"></span>Clearview<br>Optics</div>
    <div class="foot">Your address, City State, Zip 1234<br>123 456 789 · info@yourgmail.com · www.yourwebsite.com</div>
  </div>
  <div class="panel front">
    <div class="mark"></div>
    <svg class="wave" viewBox="0 0 120 16" preserveAspectRatio="none" height="16"><path d="M0 10 C30 2 70 6 120 0 L120 16 L0 16Z" fill="#0c1a28"/><path d="M0 12 C30 5 70 9 120 4 L120 16 L0 16Z" fill="#3aa8df"/></svg>
  </div>
</section>

<!-- folder inside spread -->
<section class="sheet folder-inside">
  <div class="panel"><div class="pocket-l"></div></div>
  <div class="panel">
    <div class="insert"><div class="bar"></div></div>
    <div class="pocket-r"></div>
  </div>
</section>

<!-- envelope -->
<section class="sheet envelope">
  <div class="flap"><span class="dot"></span></div>
</section>

<!-- compliment slip -->
<section class="sheet slip">
  <div class="brand brand-dark"><span class="dot"></span>Clearview<br>Optics</div>
  <div class="addr">Your address, City<br>State, Zip 1234</div>
  <svg class="wave" viewBox="0 0 195 22" preserveAspectRatio="none" height="22"><path d="M0 14 C40 0 90 4 130 12 S180 16 195 2 L195 22 L0 22Z" fill="#0c1a28"/><path d="M0 16 C40 4 90 8 130 16 S180 20 195 10 L195 22 L0 22Z" fill="#3aa8df"/></svg>
</section>

<!-- business card front -->
<section class="sheet card card-front">
  <div class="brand brand-dark"><span class="dot"></span>Clearview<br>Optics</div>
  <div class="person">
    <div class="name">DANIEL REYES</div>
    <div class="role">Managing Director</div>
    <div><span class="ico"></span>123 456 789</div>
    <div><span class="ico"></span>info@yourgmail.com</div>
    <div><span class="ico"></span>www.yourwebsite.com</div>
    <div class="gap">Your address, City<br>State, Zip 1234</div>
  </div>
  <div class="stripe"></div>
</section>

<!-- business card back -->
<section class="sheet card card-back">
  <div class="brand brand-light"><span class="dot"></span>Clearview<br>Optics</div>
</section>

<!-- wide card -->
<section class="sheet card-wide">
  <div class="brand brand-dark"><span class="dot"></span>Clearview<br>Optics</div>
  <div class="socials"><span></span><span></span><span></span><span></span><span></span></div>
  <div class="person">
    <div class="name">DANIEL REYES</div>
    <div class="role">Managing Director</div>
    <div><span class="ico"></span>123 456 789</div>
    <div><span class="ico"></span>info@yourgmail.com</div>
    <div><span class="ico"></span>www.yourwebsite.com</div>
    <div class="gap">Your address, City<br>State, Zip 1234</div>
  </div>
</section>

<!-- invoice -->
<section class="sheet invoice">
  <header class="head">
    <div class="brand brand-light"><span class="dot"></span>Clearview<br>Optics</div>
    <div class="title">INVOICE</div>
  </header>
  <div class="inv-info inv-office">OFFICE ADDRESS<br>Unit #Your address, City<br>State, Zip 1234</div>
  <div class="inv-info inv-contact"><span class="ico"></span>123 456 789<br><span class="ico"></span>info@yourgmail.com<br><span class="ico"></span>www.yourwebsite.com</div>
  <div class="inv-order">Order No:.....................<br>Page:..........................<br>Date:..........................</div>
  <table class="inv-table">
    <thead><tr><th style="width:45px">Quantity</th><th>Description</th><th style="width:44px">Amount</th></tr></thead>
    <tbody>
      <tr><td></td><td></td><td></td></tr><tr><td></td><td></td><td></td></tr>
      <tr><td></td><td></td><td></td></tr><tr><td></td><td></td><td></td></tr>
      <tr><td></td><td></td><td></td></tr><tr><td></td><td></td><td></td></tr>
      <tr><td></td><td></td><td></td></tr><tr><td></td><td></td><td></td></tr>
      <tr><td></td><td></td><td></td></tr><tr><td></td><td></td><td></td></tr>
      <tr><td></td><td></td><td></td></tr>
    </tbody>
  </table>
  <div class="totals">
    <div class="row">Sub Total <span class="box"></span></div>
    <div class="row">Tax <span class="box"></span></div>
    <div class="row total">Total <span class="box"></span></div>
  </div>
  <div class="terms">All goods remain the property of northlens.com until this invoice is paid in full. Returns or claims accepted after 7 days.</div>
  <div class="sign sign-recv">Received in good Condition</div>
  <div class="sign sign-auth">Authorised Signature</div>
  <svg class="wave" viewBox="0 0 297 34" preserveAspectRatio="none" height="34"><path d="M0 22 C60 0 120 6 190 20 S270 28 297 2 L297 34 L0 34Z" fill="#0c1a28"/><path d="M0 25 C60 6 120 12 190 26 S270 32 297 14 L297 34 L0 34Z" fill="#3aa8df"/></svg>
</section>

</body>
</html>
```